Consulting company with focus on aviation needs

We need a new business card design for our company. The company consults with multiple players in the industry like manufacturers and airlines. It is also a supplier and an inter-company level. Given the targeted industry (aviation) it should be both kind of serious, sound, secure, classy, ​​but also a bit technical, innovative. Should not be too playful, however, "fresh", "airy", "ligth" and "suprising" are suitabe attributes. The existing logo shall be used.

Industry/Entity Type

Airlines

```html
<!DOCTYPE html>
<html lang="en">
<head>
<meta charset="utf-8">
<title>Velantis Business Card</title>
<link rel="stylesheet" href="https://fonts.googleapis.com/css2?family=Questrial&display=swap">
<style>
  :root {
    --backdrop: #2a2a2a;
    --card: #f7f7f5;
    --ink: #5e5f61;
    --ink-soft: #6f7073;
    --accent: #ef9a1f;
    --rule: #b9b9b9;
    --mark: #9a9a9a;
  }
  * { margin: 0; padding: 0; box-sizing: border-box; }
  html, body {
    width: 1200px; height: 900px; overflow: hidden;
    background: var(--backdrop);
    font-family: "Questrial", "Century Gothic", sans-serif;
    color: var(--ink);
  }
  .canvas { position: relative; width: 1200px; height: 900px; }
  .card {
    position: absolute; left: 290px; width: 620px; height: 354px;
    background: var(--card);
    box-shadow: 0 8px 24px rgba(0,0,0,0.45);
  }
  .card-front { top: 50px; }
  .card-back { top: 496px; }

  /* front */
  .brand {
    position: absolute; left: 0; right: 0; top: 80px;
    display: flex; flex-direction: column; align-items: center;
  }
  .brand-dot {
    width: 66px; height: 66px; border-radius: 50%;
    background: var(--mark); margin-bottom: 14px;
  }
  .brand-name {
    font-size: 50px; letter-spacing: 10px; line-height: 1;
    color: var(--ink); padding-left: 10px;
  }
  .brand-tagline {
    margin-top: 6px; font-size: 15px; color: var(--accent); letter-spacing: 0.3px;
  }

  /* back */
  .person {
    position: absolute; left: 100px; top: 110px; width: 210px; text-align: right;
  }
  .person-name { font-size: 27px; letter-spacing: 0.5px; color: var(--ink); font-weight: 700; line-height: 1.05; white-space: nowrap; }
  .person-title { font-size: 15px; color: var(--accent); margin-top: 2px; letter-spacing: 0.5px; }
  .divider {
    position: absolute; left: 328px; top: 100px; width: 1px; height: 118px; background: var(--rule);
  }
  .contact { position: absolute; left: 346px; top: 96px; font-size: 14px; color: var(--ink-soft); }
  .contact-company { font-size: 16px; color: var(--ink); margin-left: 20px; margin-bottom: 6px; }
  .contact-list { list-style: none; }
  .contact-item { display: flex; align-items: center; gap: 8px; height: 20px; white-space: nowrap; }
  .contact-item svg { width: 12px; height: 12px; fill: var(--ink-soft); flex: none; }
  .address {
    position: absolute; left: 0; right: 0; bottom: 44px;
    display: flex; justify-content: center; align-items: center; gap: 6px;
    font-size: 15px; color: var(--ink-soft);
  }
  .address svg { width: 12px; height: 16px; fill: var(--ink-soft); }
</style>
</head>
<body>
<main class="canvas">
  <section class="card card-front">
    <div class="brand">
      <span class="brand-dot"></span>
      <span class="brand-name">VELANTIS</span>
      <span class="brand-tagline">Linking Partners - Shaping Flight</span>
    </div>
  </section>

  <section class="card card-back">
    <div class="person">
      <div class="person-name">ELIAS VARGA</div>
      <div class="person-title">CEO/FOUNDER</div>
    </div>
    <div class="divider"></div>
    <div class="contact">
      <div class="contact-company">Velantis GmbH</div>
      <ul class="contact-list">
        <li class="contact-item">
          <svg viewBox="0 0 12 12" aria-hidden="true"><path d="M2.4 0.6l1.8 2.1-1 1.2c0.7 1.6 1.8 2.8 3.4 3.6l1.2-1 2.1 1.8-0.9 2.2C5 10.3 1.5 6.8 0.5 1.5z"/></svg>
          <span>455 210 4471</span>
        </li>
        <li class="contact-item">
          <svg viewBox="0 0 12 12" aria-hidden="true"><path d="M3 0h6v12H3zM4 1.5v7.5h4V1.5zM5.5 10h1v1h-1z" fill-rule="evenodd"/></svg>
          <span>455 639 1827</span>
        </li>
        <li class="contact-item">
          <svg viewBox="0 0 12 12" aria-hidden="true"><path d="M3 0h6v3H3zM0 4h12v5h-2v3H2V9H0zM3 8v3h6V8z" fill-rule="evenodd"/></svg>
          <span>455 702 5316</span>
        </li>
        <li class="contact-item">
          <svg viewBox="0 0 12 12" aria-hidden="true"><path d="M0 2h12v1.2L6 7 0 3.2zM0 4.6l6 3.8 6-3.8V10H0z"/></svg>
          <span>info@velantis-air.com</span>
        </li>
        <li class="contact-item">
          <svg viewBox="0 0 12 12" aria-hidden="true"><circle cx="6" cy="6" r="6"/></svg>
          <span>www.velantis-air.com</span>
        </li>
      </ul>
    </div>
    <div class="address">
      <svg viewBox="0 0 12 16" aria-hidden="true"><path d="M6 0a6 6 0 0 0-6 6c0 4.5 6 10 6 10s6-5.5 6-10a6 6 0 0 0-6-6zm0 8.5a2.5 2.5 0 1 1 0-5 2.5 2.5 0 0 1 0 5z"/></svg>
      <span>2140 Harbor View Road, Anchorage, Alaska 34512</span>
    </div>
  </section>
</main>
</body>
</html>
```